Data Flow Illustrative Diagram

We'd like an illustrative diagram for a data product we are developing. The product is based in the construction industry and is a rating system for contractros.
We want to illustrate a number of states in the process.
1. Data Collection
- We have an online interface in which contractors can upload their data in multiple formats.
- Data is also collected from third party data feeds
- All Data is stored in a centralized database
2. Data Cleansing and Merging
- The collected data from all sources is cleansed and merged together
- Need to highlight that this data is secure and never shared
3. Data Prep/Ratio Calculation
- The data is then manipulated to show and prepared for a run through a financial model
- Again, need to indicate that the orginal RAW data collected in 1 and 2 is never shared
4. Model Run / Scoring
We run financial models on the data produced in Stage 3 to generate a "score/grade" for the individual contractors
5a. Dashboard - Paying Users
The contractor "score/grade" from 4 is available on a dashboard for paying users to see
5b. Dashboard - contractors
The contractor can also log into a dashboard to see their individual score along with where they rank amongst other contractors.
6. We gather contractor project review information and feed it into the model the the Dashboard/interface
7. Machine Learning / Artificial Intelligence
- We need another component off of Stage 3/4 that indicates we are running machine learning algorithms on the data to produce constantly improving results.
This illustrative diagram will be shown to contractors as well as technical companies so it should be clear and easy to understand.
Our website/company colours are purple (accented with blue).
See the two attached diagrams for very basic ideas of the flow. We'd like something much more polished and professional but extremely easy to understand.
Extending the deadline and guaranteeing the project.
- Please note that I'm looking to show a flow of data moving through a system. Not simply an itemized list
- This is in the construction industry and should reflect that.
- IMPORTANT TO HIGHLIGHT: This is a centralized database for the industry. Data is collected from multiple sources and stored in a secure central location.
Construction Industry
Construction

```html
<!DOCTYPE html>
<html lang="en">
<head>
<meta charset="utf-8">
<title>Contractor Rating Data Flow</title>
<link rel="stylesheet" href="https://fonts.googleapis.com/css2?family=Noto+Sans:wght@400;600&display=swap">
<style>
  :root {
    --bg: #f2f2f2;
    --purple-deep: #4a1f73;
    --purple: #6b3fa0;
    --purple-mid: #8a5cc4;
    --purple-soft: #b79ae0;
    --blue: #00a9c9;
    --ink: #333333;
    --ink-soft: #5f5f6b;
    --white: #ffffff;
  }
  html, body {
    margin: 0;
    padding: 0;
    overflow: hidden;
    background: var(--bg);
  }
  .canvas {
    width: 869px;
    height: 1200px;
    position: relative;
    background: var(--bg);
    overflow: hidden;
  }
  .flow {
    position: absolute;
    inset: 0;
  }
  .source-dot { fill: var(--purple-soft); }
  .stage-cleansing { fill: var(--purple); }
  .stage-prep { fill: var(--purple-mid); }
  .stage-model { fill: var(--purple-deep); }
  .stage-learning { fill: var(--blue); }
  .stage-dashboard { fill: var(--purple-soft); }
  .review-dot { fill: var(--blue); }
  .connector-thin {
    fill: none;
    stroke: var(--blue);
    stroke-width: 1.2;
  }
  .connector-main {
    fill: none;
    stroke: var(--blue);
    stroke-width: 3;
    stroke-linecap: round;
    stroke-linejoin: round;
  }
  .connector-loop {
    fill: none;
    stroke: var(--blue);
    stroke-width: 2;
    stroke-dasharray: 6 5;
    stroke-linecap: round;
  }
  .heading {
    font-family: "Noto Sans", sans-serif;
    font-weight: 600;
    font-size: 28px;
    fill: var(--purple-deep);
    text-anchor: middle;
  }
  .subheading {
    font-family: "Noto Sans", sans-serif;
    font-size: 15px;
    fill: var(--ink-soft);
    text-anchor: middle;
  }
  .stage-label {
    font-family: "Noto Sans", sans-serif;
    font-size: 22px;
    fill: var(--ink);
    text-anchor: middle;
  }
  .stage-number {
    font-family: "Noto Sans", sans-serif;
    font-weight: 600;
    font-size: 30px;
    fill: var(--white);
    text-anchor: middle;
    dominant-baseline: central;
  }
  .stage-number.small { font-size: 22px; }
  .source-label {
    font-family: "Noto Sans", sans-serif;
    font-size: 13px;
    fill: var(--ink-soft);
  }
  .source-label.centered { text-anchor: middle; }
  .secure-note {
    font-family: "Noto Sans", sans-serif;
    font-size: 13px;
    fill: var(--purple);
  }
  .lock-body { fill: var(--purple); }
  .lock-shackle { fill: none; stroke: var(--purple); stroke-width: 1.8; }
  .footer-band { fill: var(--purple-deep); }
  .footer-text {
    font-family: "Noto Sans", sans-serif;
    font-size: 14px;
    fill: var(--white);
    text-anchor: middle;
    letter-spacing: 0.5px;
  }
  .collection-illustration {
    position: absolute;
    left: 374px;
    top: 100px;
    width: 120px;
    height: 128px;
    border-radius: 32px 32px 60px 60px;
    background: linear-gradient(180deg, #e3e3e3 0%, #e3e3e3 55%, var(--blue) 56%, var(--blue) 100%);
  }
</style>
</head>
<body>
<div class="canvas">
  <svg class="flow" width="869" height="1200" viewBox="0 0 869 1200" xmlns="http://www.w3.org/2000/svg">
    <defs>
      <marker id="tip-small" markerWidth="8" markerHeight="8" refX="7" refY="4" orient="auto" markerUnits="userSpaceOnUse">
        <path d="M1,1 L7,4 L1,7" fill="none" stroke="#00a9c9" stroke-width="1.2"/>
      </marker>
      <marker id="tip-main" markerWidth="14" markerHeight="14" refX="11" refY="7" orient="auto" markerUnits="userSpaceOnUse">
        <path d="M2,1 L11,7 L2,13" fill="none" stroke="#00a9c9" stroke-width="2.4" stroke-linecap="round" stroke-linejoin="round"/>
      </marker>
      <symbol id="lock-icon" viewBox="0 0 12 14">
        <path class="lock-shackle" d="M3,6.5 V4.2 A3,3 0 0 1 9,4.2 V6.5"/>
        <rect class="lock-body" x="1" y="6" width="10" height="8" rx="1.5"/>
      </symbol>
    </defs>

    <!-- Heading -->
    <text class="heading" x="434" y="48">Contractor Rating Data Flow</text>
    <text class="subheading" x="434" y="74">One secure, centralized database for the construction industry</text>

    <!-- Stage 1 sources -->
    <g class="inputs-collection">
      <circle class="source-dot" cx="62" cy="126" r="15"/>
      <circle class="source-dot" cx="62" cy="166" r="15"/>
      <circle class="source-dot" cx="62" cy="206" r="15"/>
      <text class="source-label" x="86" y="131">Contractor uploads</text>
      <text class="source-label" x="86" y="171">Third-party feeds</text>
      <text class="source-label" x="86" y="211">Multiple formats</text>
      <path class="connector-thin" d="M228,126 H248 Q258,126 258,136 V196 Q258,206 248,206 H228"/>
      <path class="connector-thin" d="M258,166 H362" marker-end="url(#tip-small)"/>
    </g>

    <!-- Stage 1 label -->
    <text class="stage-label" x="434" y="260">1 · Data Collection</text>

    <!-- 1 to 2 -->
    <path class="connector-main" d="M500,166 H560 Q600,166 600,206 V340 Q600,380 560,380 H500" marker-end="url(#tip-main)"/>

    <!-- Stage 2 -->
    <circle class="stage-cleansing" cx="434" cy="380" r="62"/>
    <text class="stage-number" x="434" y="380">2</text>
    <text class="stage-label" x="434" y="470">Data Cleansing &amp; Merging</text>
    <use href="#lock-icon" x="362" y="481" width="12" height="14"/>
    <text class="secure-note" x="380" y="493">Secure · never shared</text>

    <!-- Stage 2 sources -->
    <g class="inputs-cleansing">
      <text class="source-label centered" x="790" y="330">Central DB</text>
      <circle class="source-dot" cx="790" cy="350" r="15"/>
      <text class="source-label centered" x="790" y="398">Validation</text>
      <circle class="source-dot" cx="790" cy="420" r="15"/>
      <path class="connector-thin" d="M770,350 H750 Q740,350 740,360 V410 Q740,420 750,420 H770"/>
      <path class="connector-thin" d="M740,385 H614" marker-end="url(#tip-small)"/>
    </g>

    <!-- 2 to 3 -->
    <path class="connector-main" d="M372,380 H320 Q280,380 280,420 V560 Q280,600 320,600 H366" marker-end="url(#tip-main)"/>

    <!-- Stage 3 -->
    <circle class="stage-prep" cx="434" cy="600" r="62"/>
    <text class="stage-number" x="434" y="600">3</text>
    <text class="stage-label" x="434" y="690">Data Prep / Ratio Calculation</text>
    <use href="#lock-icon" x="368" y="701" width="12" height="14"/>
    <text class="secure-note" x="386" y="713">Raw data never shared</text>

    <!-- Stage 3 source -->
    <g class="inputs-prep">
      <circle class="source-dot" cx="120" cy="640" r="15"/>
      <text class="source-label centered" x="120" y="674">Financial ratios</text>
      <path class="connector-thin" d="M142,640 H376" marker-end="url(#tip-small)"/>
    </g>

    <!-- 3 to 4 -->
    <path class="connector-main" d="M434,724 V762" marker-end="url(#tip-main)"/>

    <!-- Stage 7 machine learning loop -->
    <circle class="stage-learning" cx="724" cy="716" r="46"/>
    <text class="stage-number small" x="724" y="716">7</text>
    <text class="stage-label" x="724" y="790" style="font-size:18px">Machine Learning / AI</text>
    <text class="source-label centered" x="724" y="810">Constantly improving results</text>
    <path class="connector-loop" d="M494,616 Q610,630 674,694" marker-end="url(#tip-small)"/>
    <path class="connector-loop" d="M680,740 Q610,800 494,816" marker-end="url(#tip-small)"/>

    <!-- Stage 4 -->
    <circle class="stage-model" cx="434" cy="830" r="62"/>
    <text class="stage-number" x="434" y="830">4</text>
    <text class="stage-label" x="434" y="922">Model Run / Scoring</text>

    <!-- 4 to dashboards -->
    <path class="connector-main" d="M372,840 H300 Q250,840 250,890 V986" marker-end="url(#tip-main)"/>
    <path class="connector-main" d="M496,850 H568 Q618,850 618,900 V986" marker-end="url(#tip-main)"/>

    <!-- Stage 5a -->
    <circle class="stage-dashboard" cx="250" cy="1040" r="46"/>
    <text class="stage-number small" x="250" y="1040">5a</text>
    <text class="stage-label" x="250" y="1112" style="font-size:18px">Dashboard</text>
    <text class="source-label centered" x="250" y="1132">Paying users</text>

    <!-- Stage 5b -->
    <circle class="stage-dashboard" cx="618" cy="1040" r="46"/>
    <text class="stage-number small" x="618" y="1040">5b</text>
    <text class="stage-label" x="618" y="1112" style="font-size:18px">Dashboard</text>
    <text class="source-label centered" x="618" y="1132">Contractors · score &amp; rank</text>

    <!-- Stage 6 reviews feedback -->
    <circle class="review-dot" cx="434" cy="1040" r="22"/>
    <text class="stage-number small" x="434" y="1040" style="font-size:18px">6</text>
    <text class="stage-label" x="434" y="1090" style="font-size:16px">Project Reviews</text>
    <path class="connector-loop" d="M570,1040 H462" marker-end="url(#tip-small)"/>
    <path class="connector-loop" d="M434,1016 V936" marker-end="url(#tip-small)"/>

    <!-- Footer band -->
    <rect class="footer-band" x="0" y="1164" width="869" height="36"/>
    <text class="footer-text" x="434" y="1187">Construction industry data · collected from many sources · stored securely in one place</text>
  </svg>

  <div class="collection-illustration" role="img" aria-label="Illustration of a contractor at a desk uploading documents on a computer"></div>
</div>
</body>
</html>
```